Lens Deal Scout

This website is a price comparison site specialising in Digital Photographic equipment - DSLR Cameras & Lenses etc. It is going to operate along the lines of a site called www.shutterquoteroom.com
It must look much more professional and less home made than the afforementioned site. My site will be a direct competitor to shutterquoteroom, so it must look and operate much better.
The new site is first and foremost a price information site - it is not selling anything! The message it should send to visitors is one of impartiality and unbiased information, the shops it links to are the ones who will be selling products. People who visit this site, have already decided which product they are going to buy, they are now at the stage of looking for which shop is offering the best deal based on PRICE. This is NOT a "WHAT CAMERA" site. This site is comparing DIFFERENT PRICES for the same product offered by a list of SHOPS. The site should look expensive. I have a couple of Logos which you can look at for colour ideas. I like Blue, Silver, aluminium, stainless steel, White, Grey and Black. There must be lots of product category buttons to chose from. If you can come up with anything imaginative, I will appreciate any clever ideas. Some flash technology might be nice or something visually interesting happening to catch the visitors attention. There are lots of stock photos available on the net of the kind of products we will be dealing with. In particular VELMIRA and TORQUA Digital SLR Cameras and Lenses. All the other brands are definately second division. There will be no telephone number on the page. My Logo will be at the top of the page. I have uploaded two logos for you to take your pick and a very nice picture of a very expensivr DSLR camera which you might want to utilize.
Updates

Target Market(s)

Buyers of DSLR Camera equipment 70% Male, Age group 35 to 70. The products being compared on this site are all high ticket items. Customers are usually quite well off.

Industry/Entity Type

Camera

Requirements
Must have
• Must be simple and easy to navigate to find the desired product very easily.
Nice to have
• Should have a space on the front page for "TODAYS PRICE DROPS"

```html
<!DOCTYPE html>
<html lang="en">
<head>
<meta charset="utf-8">
<title>Lens Deal Scout</title>
<link href="https://fonts.googleapis.com/css2?family=Didact+Gothic&family=Mulish:wght@700&display=swap" rel="stylesheet">
<style>
:root{
  --ink:#333;
  --bar:#2c2c2c;
  --bar-edge:#1c1c1c;
  --line:#e3e3e3;
  --head-top:#f7f7f7;
  --head-bot:#e6e6e6;
  --velmira:#6a8fb3;
  --torqua:#6cb24e;
  --sorell:#d9534f;
  --pentura:#7a66b4;
  --drop:#c2738f;
  --lowest:#4fb1d2;
  --go:#5ea83a;
  --foot:#343434;
}
*{box-sizing:border-box;margin:0;padding:0}
html,body{width:1162px;height:1200px;overflow:hidden;background:#fff}
body{font-family:"Didact Gothic",sans-serif;color:var(--ink)}
.stage{position:absolute;left:5px;top:0;width:1188px;height:1239px;transform:scale(.969);transform-origin:0 0}
.hero{position:absolute;left:235px;top:0;width:765px;height:350px;
  background:radial-gradient(circle at 57% 62%,#6d5a78 0,#2a2a2e 14%,#151515 24%,#2b2b2b 45%,#1a1a1a 70%,#3a3a3a 100%);
  border-radius:0 0 30px 30px}
.updated{position:absolute;left:840px;top:0;width:175px;height:40px;background:#2a2a2a;color:#ddd;font-size:7.5px;line-height:10px;padding:10px 0 0 8px;display:flex;gap:6px;white-space:nowrap}
.updated .social{display:flex;align-items:center;border-left:1px solid #555;padding-left:6px;margin-top:-8px;color:#fff;font-size:7px}
.store{position:absolute;left:1025px;top:3px;width:104px;height:38px;background:#000;border:1px solid #888;border-radius:5px;color:#fff;display:flex;align-items:center;gap:6px;padding-left:8px}
.store .dot{width:14px;height:14px;background:#fff;border-radius:50%}
.store small{display:block;font-size:6px;letter-spacing:.5px}
.store b{font-weight:normal;font-size:14px}
.nav{position:absolute;left:190px;top:296px;width:826px;height:46px;background:var(--bar);border-bottom:2px solid var(--bar-edge);display:flex;align-items:center;padding-left:10px}
.nav a{color:#fff;text-decoration:none;font-size:14px;padding:5px 10px;border-right:1px solid #444}
.nav a.active{background:#1b1b1b}
.search{position:absolute;left:590px;top:10px;display:flex}
.search span{width:193px;height:25px;background:linear-gradient(#fff,#ddd);border-radius:3px 0 0 3px;color:#999;font-size:13px;padding:4px 9px;font-style:italic}
.search b{width:30px;height:25px;background:var(--go);color:#fff;font-weight:normal;font-size:14px;text-align:center;line-height:25px;border-radius:0 3px 3px 0}
.panel{position:absolute;width:318px}
.panel h2,.side h2{height:41px;background:linear-gradient(var(--head-top),var(--head-bot));font-family:"Mulish",sans-serif;font-size:12.5px;text-align:center;line-height:44px;color:#222}
.row{height:25px;border-bottom:1px solid var(--line);display:flex;align-items:center;font-size:11.5px;padding-left:10px;white-space:nowrap}
.row .name{flex:1}
.row .price{width:40px;text-align:right;margin-right:8px}
.btn{width:32px;height:14px;color:#fff;font-size:11px;line-height:14px;text-align:center;margin-right:6px}
.velmira .btn{background:var(--velmira)}
.torqua .btn{background:var(--torqua)}
.sorell .btn{background:var(--sorell)}
.pentura .btn{background:var(--pentura)}
.side{position:absolute;left:856px;width:212px}
.deal{height:49px;border-bottom:1px solid var(--line);padding:5px 0 0 10px;position:relative}
.deal p{font-size:11.5px}
.deal small{display:block;font-size:7.5px;line-height:11px;margin-top:3px}
.deal i{position:absolute;right:4px;top:23px;width:33px;height:14px;color:#fff;font-style:normal;font-size:11px;line-height:14px;text-align:center}
.drop i{background:var(--drop)}
.low i{background:var(--lowest)}
.footer{position:absolute;left:121px;top:1201px;width:946px;height:38px;background:var(--foot);color:#aaa;font-size:9.5px;padding:16px 0 0 18px}
</style>
</head>
<body>
<div class="stage">
  <div class="hero" role="img" aria-label="Close-up photo of a black DSLR camera body with a large lens"></div>

  <div class="updated"><span>Last Update: 15:44<br>Sunday 19/08/12</span><span class="social">Friendwall Circlio Chirpet</span></div>
  <div class="store"><span class="dot"></span><span><small>GET THE APP ON</small><b>Appvault</b></span></div>

  <nav class="nav">
    <a class="active">Home</a><a>Velmira</a><a>Torqua</a><a>Orvane</a><a>Sorell</a><a>Pentura</a><a>Panaro</a><a>Other Equipments</a>
    <div class="search"><span>search</span><b>Go</b></div>
  </nav>

  <section class="panel velmira" style="left:190px;top:352px">
    <h2>Velmira Digital SLRs</h2>
    <div class="row"><span class="name">VX 210 Body</span><span class="price">$599</span><span class="btn">view</span></div>
    <div class="row"><span class="name">VX 210 Body Kit 20-60 ST Lens</span><span class="price">$799</span><span class="btn">view</span></div>
    <div class="row"><span class="name">VX 210 Body</span><span class="price">$599</span><span class="btn">view</span></div>
    <div class="row"><span class="name">VX 210 Body</span><span class="price">$599</span><span class="btn">view</span></div>
    <div class="row"><span class="name">VX 210 Body</span><span class="price">$599</span><span class="btn">view</span></div>
    <div class="row"><span class="name">VX 210 Body</span><span class="price">$599</span><span class="btn">view</span></div>
    <div class="row"><span class="name">VX 210 Body</span><span class="price">$599</span><span class="btn">view</span></div>
    <div class="row"><span class="name">VX 210 Body</span><span class="price">$599</span><span class="btn">view</span></div>
    <div class="row"><span class="name">VX 210 Body</span><span class="price">$599</span><span class="btn">view</span></div>
    <div class="row"><span class="name">VX 210 Body</span><span class="price">$599</span><span class="btn">view</span></div>
    <div class="row"><span class="name">VX 210 Body</span><span class="price">$599</span><span class="btn">view</span></div>
    <div class="row"><span class="name">VX 210 Body</span><span class="price">$599</span><span class="btn">view</span></div>
    <div class="row"><span class="name">VX 210 Body</span><span class="price">$599</span><span class="btn">view</span></div>
    <div class="row"><span class="name">VX 210 Body</span><span class="price">$599</span><span class="btn">view</span></div>
    <div class="row"><span class="name">VX 210 Body</span><span class="price">$599</span><span class="btn">view</span></div>
    <div class="row"><span class="name">VX 210 Body</span><span class="price">$599</span><span class="btn">view</span></div>
    <div class="row"><span class="name">VX 210 Body</span><span class="price">$599</span><span class="btn">view</span></div>
    <div class="row"><span class="name">VX 210 Body</span><span class="price">$599</span><span class="btn">view</span></div>
    <div class="row"><span class="name">VX 210 Body</span><span class="price">$599</span><span class="btn">view</span></div>
    <div class="row"><span class="name">VX 210 Body</span><span class="price">$599</span><span class="btn">view</span></div>
    <div class="row"><span class="name">VX 210 Body</span><span class="price">$599</span><span class="btn">view</span></div>
  </section>

  <section class="panel pentura" style="left:190px;top:936px">
    <h2>Pentura Digital SLRs</h2>
    <div class="row"><span class="name">VX 210 Body</span><span class="price">$599</span><span class="btn">view</span></div>
    <div class="row"><span class="name">VX 210 Body Kit 20-60 ST Lens</span><span class="price">$799</span><span class="btn">view</span></div>
    <div class="row"><span class="name">VX 210 Body</span><span class="price">$599</span><span class="btn">view</span></div>
    <div class="row"><span class="name">VX 210 Body</span><span class="price">$599</span><span class="btn">view</span></div>
    <div class="row"><span class="name">VX 210 Body</span><span class="price">$599</span><span class="btn">view</span></div>
    <div class="row"><span class="name">VX 210 Body</span><span class="price">$599</span><span class="btn">view</span></div>
    <div class="row"><span class="name">VX 210 Body</span><span class="price">$599</span><span class="btn">view</span></div>
    <div class="row"><span class="name">VX 210 Body</span><span class="price">$599</span><span class="btn">view</span></div>
    <div class="row"><span class="name">VX 210 Body</span><span class="price">$599</span><span class="btn">view</span></div>
  </section>

  <section class="panel torqua" style="left:523px;top:352px">
    <h2>Torqua Digital SLRs</h2>
    <div class="row"><span class="name">VX 210 Body</span><span class="price">$599</span><span class="btn">view</span></div>
    <div class="row"><span class="name">VX 210 Body Kit 20-60 ST Lens</span><span class="price">$799</span><span class="btn">view</span></div>
    <div class="row"><span class="name">VX 210 Body</span><span class="price">$599</span><span class="btn">view</span></div>
    <div class="row"><span class="name">VX 210 Body</span><span class="price">$599</span><span class="btn">view</span></div>
    <div class="row"><span class="name">VX 210 Body</span><span class="price">$599</span><span class="btn">view</span></div>
    <div class="row"><span class="name">VX 210 Body</span><span class="price">$599</span><span class="btn">view</span></div>
    <div class="row"><span class="name">VX 210 Body</span><span class="price">$599</span><span class="btn">view</span></div>
    <div class="row"><span class="name">VX 210 Body</span><span class="price">$599</span><span class="btn">view</span></div>
    <div class="row"><span class="name">VX 210 Body</span><span class="price">$599</span><span class="btn">view</span></div>
    <div class="row"><span class="name">VX 210 Body</span><span class="price">$599</span><span class="btn">view</span></div>
    <div class="row"><span class="name">VX 210 Body</span><span class="price">$599</span><span class="btn">view</span></div>
    <div class="row"><span class="name">VX 210 Body</span><span class="price">$599</span><span class="btn">view</span></div>
    <div class="row"><span class="name">VX 210 Body</span><span class="price">$599</span><span class="btn">view</span></div>
    <div class="row"><span class="name">VX 210 Body</span><span class="price">$599</span><span class="btn">view</span></div>
    <div class="row"><span class="name">VX 210 Body</span><span class="price">$599</span><span class="btn">view</span></div>
    <div class="row"><span class="name">VX 210 Body</span><span class="price">$599</span><span class="btn">view</span></div>
  </section>

  <section class="panel sorell" style="left:523px;top:816px">
    <h2>Sorell Digital SLRs</h2>
    <div class="row"><span class="name">VX 210 Body</span><span class="price">$599</span><span class="btn">view</span></div>
    <div class="row"><span class="name">VX 210 Body Kit 20-60 ST Lens</span><span class="price">$799</span><span class="btn">view</span></div>
    <div class="row"><span class="name">VX 210 Body</span><span class="price">$599</span><span class="btn">view</span></div>
    <div class="row"><span class="name">VX 210 Body</span><span class="price">$599</span><span class="btn">view</span></div>
    <div class="row"><span class="name">VX 210 Body</span><span class="price">$599</span><span class="btn">view</span></div>
    <div class="row"><span class="name">VX 210 Body</span><span class="price">$599</span><span class="btn">view</span></div>
    <div class="row"><span class="name">VX 210 Body</span><span class="price">$599</span><span class="btn">view</span></div>
    <div class="row"><span class="name">VX 210 Body</span><span class="price">$599</span><span class="btn">view</span></div>
    <div class="row"><span class="name">VX 210 Body</span><span class="price">$599</span><span class="btn">view</span></div>
    <div class="row"><span class="name">VX 210 Body</span><span class="price">$599</span><span class="btn">view</span></div>
    <div class="row"><span class="name">VX 210 Body</span><span class="price">$599</span><span class="btn">view</span></div>
    <div class="row"><span class="name">VX 210 Body</span><span class="price">$599</span><span class="btn">view</span></div>
    <div class="row"><span class="name">VX 210 Body</span><span class="price">$599</span><span class="btn">view</span></div>
    <div class="row"><span class="name">VX 210 Body</span><span class="price">$599</span><span class="btn">view</span></div>
  </section>

  <aside class="side drop" style="top:352px">
    <h2>Price Drop Today</h2>
    <div class="deal"><p>VX 210 Body</p><small>A drop of $3.8 in the price at<br>www.shopmartex.com</small><i>more</i></div>
    <div class="deal"><p>VX 480 Body</p><small>A drop of $3.8 in the price at<br>www.shopmartex.com</small><i>more</i></div>
  </aside>

  <aside class="side drop" style="top:509px">
    <h2>New Lowest Ever Price</h2>
    <div class="deal"><p>VX 210 Body</p><small>A drop of $3.8 in the price at<br>www.shopmartex.com</small><i>more</i></div>
    <div class="deal"><p>VX 480 Body</p><small>A drop of $3.8 in the price at<br>www.shopmartex.com</small><i>more</i></div>
  </aside>

  <aside class="side low" style="top:666px">
    <h2>Lowest Ever Price</h2>
    <div class="deal"><p>VX 210 Body</p><small>A drop of $3.8 in the price at<br>www.shopmartex.com</small><i>more</i></div>
    <div class="deal"><p>VX 480 Body</p><small>A drop of $3.8 in the price at<br>www.shopmartex.com</small><i>more</i></div>
  </aside>

  <footer class="footer">All Rights reserved</footer>
</div>
</body>
</html>
```